Website for software company "velbra"

We need a website for our software company/startup named "velbra". We are developing several products (currently 3 standard-software products) which are all in different sectors, but all our products are available for Laptops/PC/Mobile Phones/Tablets, ... We do also create custom software and support our customers with consulting to optimize their processes.
We already have a Logo which you can find in the attached files.
We are a young team of 4 members (two founders and 2 employees).

To get an idea of our products -> the first one is a planning software for healthcare organizations (eg. Mercyway, firebrigade, pharmacy), the second one is a booking software for sport clubs and the third one is a competition software for sports hunting. You see very diverse. Include or ignore this info of our products as you like.

The design has to be a bootstrap 4 (or higher) design. We have licenced FontAwesome as iconset. Responsive design should come without saying.

Coding

Coded - Design and coding required

Number of Pages Required

5+ page

Font styles to use
Sans Serif

Requirements
Must have
• Starting page, product pages, news section, contact, team, services

```html
<!DOCTYPE html>
<html lang="en">
<head>
<meta charset="utf-8">
<title>velbra — Software for every sector</title>
<link rel="stylesheet" href="https://fonts.googleapis.com/css2?family=Montserrat:wght@300;400;500;600;700;800&family=Lato:wght@400;700&family=Raleway:wght@400;500&display=swap">
<style>
:root{
  --orange:#ee8a3c;
  --orange-band:#e8884a;
  --navy:#1f2936;
  --ink:#222;
  --grey:#777;
  --white:#fff;
  --black:#000;
  --peach:#fdf1e6;
  --soft-grey:#eeeeee;
}
*{box-sizing:border-box;margin:0;padding:0}
html,body{width:1200px;height:3409px;overflow:hidden}
body{position:relative;background:var(--white);font-family:"Montserrat",sans-serif;color:var(--ink)}
.abs{position:absolute}
a{color:inherit;text-decoration:none}

/* header */
.site-header{position:absolute;left:0;top:0;width:1200px;height:78px;background:var(--white)}
.brand{position:absolute;left:110px;top:14px;font-family:"Montserrat",sans-serif;font-weight:700;font-size:46px;letter-spacing:1px;color:var(--navy);line-height:1}
.main-nav{position:absolute;left:461px;top:31px;font-size:17px;font-weight:500}
.main-nav a{position:absolute;white-space:nowrap;color:var(--navy)}
.main-nav .active{color:var(--orange)}
.main-nav .active::after{content:"";position:absolute;left:50%;top:26px;width:5px;height:5px;margin-left:-2px;border-radius:50%;background:var(--orange)}
.btn-login{position:absolute;left:960px;top:21px;width:129px;height:43px;border-radius:14px;background:var(--orange);color:var(--white);font-size:17px;font-weight:500;display:flex;align-items:center;justify-content:center}

/* hero */
.hero{position:absolute;left:0;top:78px;width:1200px;height:591px;overflow:hidden}
.hero-photo{position:absolute;inset:0;background:linear-gradient(100deg,#d9dcdf 0%,#b9bfc6 40%,#8a8f96 65%,#c9a27a 85%,#5a6270 100%)}
.hero-title{position:absolute;left:110px;top:140px;color:var(--white);line-height:1}
.hero-title .small{display:block;font-weight:300;font-size:48px;letter-spacing:1px}
.hero-title .big{display:block;font-weight:700;font-size:60px;margin-top:12px;letter-spacing:1px}
.hero-text{position:absolute;left:111px;top:277px;width:340px;color:var(--white);font-size:16px;line-height:26px}
.btn-start{position:absolute;left:111px;top:376px;width:163px;height:52px;border-radius:12px;background:var(--white);color:var(--navy);font-size:17px;font-weight:500;display:flex;align-items:center;justify-content:center}

/* about */
.about-heading{position:absolute;left:0;top:748px;width:1200px;text-align:center;line-height:1}
.about-heading .a1{display:block;font-size:35px;font-weight:500;color:var(--navy)}
.about-heading .a2{display:block;font-size:42px;font-weight:700;color:var(--orange);margin-top:12px}
.about-text{position:absolute;left:143px;top:863px;width:915px;text-align:center;font-family:"Lato",sans-serif;font-size:14.6px;line-height:25.7px;color:#333}
.btn-dark{position:absolute;left:530px;top:1067px;width:141px;height:51px;border-radius:26px;background:var(--navy);color:var(--white);font-family:"Lato",sans-serif;font-weight:700;font-size:14px;display:flex;align-items:center;justify-content:center}

/* software */
.software{position:absolute;left:0;top:1247px;width:1200px;height:674px;background:var(--orange-band)}
.section-title{position:absolute;left:0;width:1200px;text-align:center;font-weight:700;font-size:30px;color:var(--navy);letter-spacing:.3px}
.product-card{position:absolute;top:136px;width:322px;height:411px;background:var(--white);text-align:center}
.product-card .thumb{position:absolute;left:8px;top:8px;width:306px;height:202px}
.product-card h3{position:absolute;left:10px;right:10px;top:228px;font-size:22px;font-weight:600;color:var(--orange);line-height:34px;text-transform:uppercase}
.product-card p{position:absolute;left:18px;right:18px;font-size:18px;line-height:25px;color:var(--ink)}
.product-card .more{position:absolute;left:0;right:0;top:372px;font-size:18px;font-weight:500;text-decoration:underline;text-underline-offset:3px;color:var(--ink)}
.arrow{position:absolute;top:340px}

/* testimonials */
.tcard{position:absolute;left:111px;width:353px;height:75px;background:var(--white)}
.tcard.raised{box-shadow:0 3px 10px rgba(0,0,0,.15)}
.avatar{position:absolute;left:17px;top:9px;width:60px;height:60px;border-radius:50%;background:linear-gradient(135deg,#c9b3a3,#6d5b50)}
.tname{position:absolute;left:89px;top:14px;font-size:20px;font-weight:500;color:var(--navy)}
.trole{position:absolute;left:90px;top:42px;font-size:13px;color:var(--grey)}
.quote-title{position:absolute;left:523px;top:2090px;font-size:22px;font-weight:600;color:var(--navy)}
.stars{position:absolute;left:523px;top:2125px;display:flex;gap:11px}
.quote-text{position:absolute;left:528px;top:2168px;width:543px;text-align:justify;font-family:"Raleway",sans-serif;font-size:14.6px;line-height:25.7px;color:#666}

/* blog */
.blog-img{position:absolute}
.blog-card{position:absolute;top:2668px;width:295px;height:218px;background:var(--white);padding:22px 19px 0}
.blog-card.lined{border-bottom:4px solid #555c66}
.blog-card.raised{height:210px;box-shadow:0 6px 14px rgba(238,138,60,.18)}
.blog-date{font-size:15px;font-weight:600;color:var(--navy)}
.blog-card.raised .blog-date{color:var(--orange)}
.blog-card h4{margin-top:20px;font-size:17px;font-weight:700;line-height:26px;color:var(--navy)}
.blog-card p{margin-top:10px;font-family:"Raleway",sans-serif;font-size:15px;line-height:25.7px;color:#888}

/* footer */
.site-footer{position:absolute;left:0;top:2973px;width:1200px;height:436px;background:var(--black);color:var(--white)}
.site-footer *{color:var(--white)}
.footer-brand{position:absolute;left:111px;top:78px;font-size:56px;font-weight:700;letter-spacing:1px;line-height:1}
.footer-about{position:absolute;left:114px;top:160px;width:290px;font-family:"Lato",sans-serif;font-size:15.5px;line-height:24px}
.social{position:absolute;left:114px;top:250px;display:flex;gap:14px;align-items:center}
.social span{width:36px;height:36px;border-radius:50%;border:1.5px solid rgba(255,255,255,.7)}
.social span.on{background:var(--orange);border-color:var(--orange)}
.fcol{position:absolute;top:78px}
.fcol h5{font-size:19px;font-weight:700;letter-spacing:.5px}
.fcol ul{list-style:none;margin-top:26px}
.fcol li{font-size:15.5px;line-height:28.5px;font-family:"Lato",sans-serif}
.fcol.bold li{font-weight:700}
.loc-row{position:absolute;left:841px;display:flex;align-items:flex-start;gap:16px;font-family:"Lato",sans-serif;font-size:15.5px;line-height:26px}
.loc-icon{width:33px;height:33px;border-radius:50%;border:1.5px solid var(--white);flex:none;display:flex;align-items:center;justify-content:center}
.footer-rule{position:absolute;left:111px;top:329px;width:977px;height:1px;background:rgba(255,255,255,.4)}
.copyright{position:absolute;left:0;top:363px;width:1200px;text-align:center;font-family:Arial,sans-serif;font-size:14px}
</style>
</head>
<body>

<header class="site-header">
  <a class="brand" href="#">VELBRA</a>
  <nav class="main-nav">
    <a class="active" style="left:0">Home</a>
    <a style="left:87px">About</a>
    <a style="left:174px">Our Software</a>
    <a style="left:324px">Blog</a>
    <a style="left:399px">Contact</a>
  </nav>
  <a class="btn-login" href="#">LOGIN</a>
</header>

<section class="hero">
  <div class="hero-photo" role="img" aria-label="Photo of two smiling colleagues looking at a screen in a bright office"></div>
  <svg class="abs" style="left:0;top:0" width="480" height="591" viewBox="0 0 480 591">
    <polygon points="0,115 472,320 120,591 0,591" fill="#232b35"/>
    <polygon points="0,40 335,40 472,320 0,115" fill="#ee8a3c" opacity=".95"/>
    <polygon points="335,8 472,8 472,320 335,250" fill="#ee8a3c"/>
  </svg>
  <h1 class="hero-title"><span class="small">WELCOME TO</span><span class="big">VELBRA</span></h1>
  <p class="hero-text">Lorem ipsum dolor sit amet, consectetur adipiscing elit, sed do eiusmod tempor incididunt .</p>
  <a class="btn-start" href="#">Get Started</a>
</section>

<section class="about">
  <svg class="abs" style="left:330px;top:745px" width="530" height="425" viewBox="0 0 530 425">
    <polygon points="12,0 400,200 400,425 12,140" fill="#fdf1e6"/>
    <polygon points="380,0 530,0 530,425 380,345" fill="#fdf1e6"/>
    <polygon points="2,160 230,300 2,416" fill="#ececec"/>
  </svg>
  <h2 class="about-heading"><span class="a1">About</span><span class="a2">VELBRA</span></h2>
  <p class="about-text">Sed ut perspiciatis unde omnis iste natus error sit voluptatem accusantium doloremque laudantium, totam rem aperiam, eaque ipsa quae ab illo inventore veritatis et quasi architecto beatae vitae dicta sunt explicabo. Nemo enim ipsam voluptatem quia voluptas sit aspernatur aut odit aut fugit, sed quia consequuntur magni dolores eos qui ratione voluptatem sequi nesciunt. Neque porro quisquam est, qui dolorem ipsum quia dolor sit amet, consectetur, adipisci velit, sed quia non numquam eius modi tempora incidunt ut labore et dolore magnam aliquam quaerat voluptatem. Ut enim ad minima veniam, quis nostrum exercitationem ullam corporis suscipit laboriosam, nisi ut aliquid ex ea commodi consequatur? Quis autem vel eum iure reprehenderit qui in ea voluptate velit esse quam nihil molestiae consequatur, vel illum qui dolorem eum fugiat quo voluptas nulla pariatur</p>
  <a class="btn-dark" href="#">Read More</a>
</section>

<section class="software">
  <h2 class="section-title" style="top:55px">OUR SOFTWARE</h2>
  <svg class="arrow" style="left:52px" width="22" height="42" viewBox="0 0 22 42"><polyline points="20,2 2,21 20,40" fill="none" stroke="#c76a30" stroke-width="2"/></svg>
  <svg class="arrow" style="left:1140px" width="22" height="42" viewBox="0 0 22 42"><polyline points="2,2 20,21 2,40" fill="none" stroke="#1f2936" stroke-width="2.5"/></svg>

  <article class="product-card" style="left:103px">
    <div class="thumb" role="img" aria-label="Photo of a medical team discussing around a tablet" style="background:linear-gradient(135deg,#6b5a4c,#c9c2b8 50%,#3d3a3a)"></div>
    <h3>Healthcare<br>Organizations</h3>
    <p style="top:307px">Nemo enim ipsam voluptatem quia voluptas sit aspernatur</p>
    <a class="more" href="#">Read More</a>
  </article>
  <article class="product-card" style="left:440px">
    <div class="thumb" role="img" aria-label="Photo of young footballers in red shirts celebrating together" style="background:linear-gradient(135deg,#7fa35a,#c8302d 45%,#d94a3c 70%,#8a9c60)"></div>
    <h3>Sport Clubs</h3>
    <p style="top:272px">Nemo enim ipsam voluptatem quia voluptas sit aspernatur magni dolores eos qui ratione</p>
    <a class="more" href="#">Read More</a>
  </article>
  <article class="product-card" style="left:775px">
    <div class="thumb" role="img" aria-label="Photo of a hunter aiming a scoped rifle outdoors" style="background:linear-gradient(135deg,#b89a5a,#4b3a2a 50%,#2a2622)"></div>
    <h3>Sports Hunting</h3>
    <p style="top:266px">Nemo enim ipsam voluptatem quia voluptas sit aspernatur magni dolores eos qui ratione</p>
    <a class="more" href="#">Read More</a>
  </article>
</section>

<section class="testimonials">
  <h2 class="section-title" style="top:2000px">TESTIMONIALS</h2>
  <div class="tcard raised" style="top:2093px">
    <div class="avatar" role="img" aria-label="Portrait photo of Corwin Hale"></div>
    <div class="tname">Corwin Hale</div>
    <div class="trole">Nemo enim ipsam voluptatem</div>
  </div>
  <div class="tcard" style="top:2197px">
    <div class="avatar" role="img" aria-label="Portrait photo of Ravi Dunmore"></div>
    <div class="tname">Ravi Dunmore</div>
    <div class="trole">Nemo enim ipsam voluptatem</div>
  </div>
  <h3 class="quote-title">Duis aute irure dolor</h3>
  <div class="stars">
    <svg width="20" height="20" viewBox="0 0 24 24"><polygon points="12,1 15,9 23,9 17,14 19,22 12,17 5,22 7,14 1,9 9,9" fill="#f4a21e"/></svg>
    <svg width="20" height="20" viewBox="0 0 24 24"><polygon points="12,1 15,9 23,9 17,14 19,22 12,17 5,22 7,14 1,9 9,9" fill="#f4a21e"/></svg>
    <svg width="20" height="20" viewBox="0 0 24 24"><polygon points="12,1 15,9 23,9 17,14 19,22 12,17 5,22 7,14 1,9 9,9" fill="#f4a21e"/></svg>
    <svg width="20" height="20" viewBox="0 0 24 24"><polygon points="12,1 15,9 23,9 17,14 19,22 12,17 5,22 7,14 1,9 9,9" fill="#f4a21e"/></svg>
    <svg width="20" height="20" viewBox="0 0 24 24"><polygon points="12,1 15,9 23,9 17,14 19,22 12,17 5,22 7,14 1,9 9,9" fill="#f4a21e"/></svg>
  </div>
  <p class="quote-text">Nemo enim ipsam voluptatem quia voluptas sit aspernatur aut odit aut fugit, sed quia consequuntur magni dolores eos qui ratione voluptatem sequi nesciunt. Neque porro quisquam est, qui dolorem ipsum quia dolor sit amet, consectetur, adipisci velit, sed quia non numquam eius modi tempora incidunt ut labore et dolore magnam aliquam quaerat voluptatem.</p>
</section>

<section class="blog">
  <h2 class="section-title" style="top:2400px">LATEST BLOG</h2>
  <div class="blog-img" role="img" aria-label="Photo of two colleagues reviewing work at a computer" style="left:63px;top:2465px;width:340px;height:253px;background:linear-gradient(135deg,#e8eaec,#a9b0b8 50%,#4a4f57)"></div>
  <div class="blog-img" role="img" aria-label="Photo of a team working together at a table in a brick-walled office" style="left:402px;top:2472px;width:351px;height:240px;background:linear-gradient(135deg,#8a5a3e,#c7a27e 45%,#5a4a3e)"></div>
  <div class="blog-img" role="img" aria-label="Photo of a cheering team raising their arms in an office" style="left:753px;top:2474px;width:359px;height:238px;background:linear-gradient(135deg,#d8d2c8,#a85a4a 50%,#6a5a4e)"></div>

  <article class="blog-card lined" style="left:111px">
    <div class="blog-date">16 APR 2022</div>
    <h4>LOREM IPSUM DOLOR SIT AMET, CONSECTETUR</h4>
    <p>Duis aute irure dolor in &nbsp;in volupta velit esse cillum dolore eu fugiat nulla pariatur.</p>
  </article>
  <article class="blog-card raised" style="left:449px">
    <div class="blog-date">16 APR 2022</div>
    <h4>LOREM IPSUM DOLOR SIT AMET, CONSECTETUR</h4>
    <p>Duis aute irure dolor in &nbsp;in volupta velit esse cillum dolore eu fugiat nulla pariatur.</p>
  </article>
  <article class="blog-card lined" style="left:791px">
    <div class="blog-date">16 APR 2022</div>
    <h4>LOREM IPSUM DOLOR SIT AMET, CONSECTETUR</h4>
    <p>Duis aute irure dolor in &nbsp;in volupta velit esse cillum dolore eu fugiat nulla pariatur.</p>
  </article>
</section>

<footer class="site-footer">
  <div class="footer-brand">VELBRA</div>
  <p class="footer-about">Duis aute irure dolor in reprehenderit in voluptate velit esse cillum dolore eu fugiat nulla pariatur</p>
  <div class="social"><span></span><span class="on"></span><span></span><span></span></div>

  <div class="fcol" style="left:425px">
    <h5>NAVIGATION</h5>
    <ul><li>Home</li><li>About</li><li>Our Software</li><li>Blog</li><li>Contact</li></ul>
  </div>
  <div class="fcol bold" style="left:617px">
    <h5>QUICK LINKS</h5>
    <ul><li>Terms&amp;condtions</li><li>Privacy Policy</li><li>About Us</li><li>Support</li></ul>
  </div>
  <div class="fcol" style="left:841px"><h5>OUR LOCATION</h5></div>

  <div class="loc-row" style="top:133px">
    <span class="loc-icon"><svg width="16" height="18" viewBox="0 0 16 20"><path d="M8 1a6 6 0 0 0-6 6c0 5 6 12 6 12s6-7 6-12a6 6 0 0 0-6-6z" fill="none" stroke="#fff" stroke-width="1.6"/><circle cx="8" cy="7" r="2.2" fill="none" stroke="#fff" stroke-width="1.6"/></svg></span>
    <span>2207 &nbsp;Lorem ipsum sit amet<br>in volupta</span>
  </div>
  <div class="loc-row" style="top:207px">
    <span class="loc-icon"><svg width="16" height="16" viewBox="0 0 24 24"><path d="M5 3h4l2 5-3 2a12 12 0 0 0 6 6l2-3 5 2v4a2 2 0 0 1-2 2A18 18 0 0 1 3 5a2 2 0 0 1 2-2z" fill="none" stroke="#fff" stroke-width="1.8"/></svg></span>
    <span style="padding-top:3px">+1 555 014 2290</span>
  </div>
  <div class="loc-row" style="top:272px">
    <span class="loc-icon"><svg width="16" height="14" viewBox="0 0 24 18"><rect x="1" y="1" width="22" height="16" rx="2" fill="none" stroke="#fff" stroke-width="1.8"/><polyline points="1,2 12,10 23,2" fill="none" stroke="#fff" stroke-width="1.8"/></svg></span>
    <span style="padding-top:3px">Info@velbra.com</span>
  </div>

  <div class="footer-rule"></div>
  <p class="copyright">© copyrights 2022 &nbsp;velbra | &nbsp;All Rights Reserved</p>
</footer>

</body>
</html>
```